依頼詳細
http://www.kobarinu.com/のトップページのリニューアルを考えており
そちらのご提案をいただきたいという業務内容です。
コンテンツはそのままで、デザインのみ作成していただきたいというものです。
コーティングなどはございません。
サイズなども特に指定はありません。
イラストレーターにて納品をお願いいたします。
ページ数
1ページ
希望イメージ
シンプル 複雑
単色 カラフル
暗い 明るい
日常 高級
遊び心 厳粛
未来的 伝統的
女性的 男性的
希望する色
青系
納品ファイル
• イラストレーター形式 (.ai)
補足説明
よろしくお願いいたします。
■ 選んだ理由

社内で選定し、一番イメージに近いものを採用させて頂きました。

■ 提案者全員のお礼・コメント

今回弊社のコンペにたくさんの応募をしていただき真に感謝しております。
どの作品も素晴らしいものばかりで、最後まで選定に時間が掛かりました。
また機会がございましたら是非みなさまのお力をお借りさせて下さい。
ありがとうございました。

```html
<!DOCTYPE html>
<html lang="ja">
<head>
<meta charset="utf-8">
<title>青嶺コンクリート工業株式会社</title>
<link href="https://fonts.googleapis.com/css2?family=Noto+Sans+JP:wght@400;500;700;900&display=swap" rel="stylesheet">
<style>
:root{
  --blue:#2b7fc8;
  --blue-dark:#1d5f9e;
  --blue-light:#5aa7e0;
  --red:#c8202a;
  --green:#3a9a3a;
  --ink:#333;
  --muted:#777;
  --line:#d7d7d7;
  --bg:#ffffff;
  --grey:#9a9a9a;
  --grey-dark:#5e5e5e;
  --tab:#6b6b6b;
  --sky:#9fc5e3;
  --water:#5e8fae;
}
*{box-sizing:border-box;margin:0;padding:0}
html,body{width:1200px;height:3080px;overflow:hidden;background:var(--bg);font-family:"Noto Sans JP",sans-serif;color:var(--ink)}
.page{width:1200px;height:3080px;position:relative;display:flex;flex-direction:column}
.wrap{width:1100px;margin:0 auto;position:relative}

/* header */
.header{height:130px}
.header .wrap{height:130px;display:flex;align-items:center;justify-content:space-between}
.brand{display:flex;align-items:center;gap:14px;font-weight:700;font-size:26px;color:var(--red)}
.brand .dot{width:26px;height:26px;border-radius:50%;background:var(--red);flex:none}
.util{display:flex;align-items:center;gap:26px;font-size:17px;color:var(--blue)}
.login{background:var(--blue);color:#fff;padding:10px 22px;border-radius:4px;font-weight:500}

/* global nav */
.gnav{border-top:1px solid var(--line);border-bottom:4px solid var(--blue);height:62px}
.gnav ul{display:flex;list-style:none;width:1100px;margin:0 auto;height:58px}
.gnav li{flex:1;text-align:center;line-height:54px;font-size:19px;color:var(--muted);border-right:1px solid var(--line)}
.gnav li:first-child{color:var(--ink);font-weight:700;border-bottom:4px solid var(--ink)}
.gnav li:last-child{border-right:none}

/* hero */
.hero{height:430px;position:relative;background:linear-gradient(180deg,var(--sky) 0%,#d7e7f2 38%,var(--water) 40%,#406f8f 100%)}
.hero-card{position:absolute;right:50px;top:220px;width:560px;background:rgba(255,255,255,.92);padding:20px 28px}
.hero-card .kicker{font-size:20px;color:var(--ink)}
.hero-card h1{font-size:38px;color:var(--blue-dark);font-weight:900;margin:4px 0 8px}
.hero-card p{font-size:17px;color:var(--ink)}

/* product tabs */
.ptabs{display:flex;width:1100px;margin:0 auto;height:100px;gap:4px;list-style:none}
.ptabs li{flex:1;background:var(--tab);color:#fff;font-size:16px;display:flex;align-items:center;justify-content:center;text-align:center;line-height:1.3}
.ptabs li.on{background:#fff;color:var(--ink);font-weight:700;border:2px solid var(--tab);border-top:none}

/* sections */
.sec-title{font-size:28px;font-weight:700;padding:40px 0 20px;border-bottom:2px solid var(--line);margin-bottom:24px}
.scenes{display:grid;grid-template-columns:repeat(5,1fr);gap:28px 16px}
.scene .ph{height:170px;border:1px solid var(--line)}
.scene .cap{text-align:center;font-size:17px;color:var(--blue);padding:12px 4px;border:1px solid var(--line);border-top:none;white-space:nowrap}
.t1{background:linear-gradient(160deg,#b9c4c9,#7d8a80)}
.t2{background:linear-gradient(160deg,#c3ccd1,#8f9895)}
.t3{background:linear-gradient(160deg,#9cc3df,#5f8aa7)}
.t4{background:linear-gradient(160deg,#a9c9e6,#2b4d7a)}
.t5{background:linear-gradient(160deg,#8aa08c,#5c6b5a)}
.t6{background:linear-gradient(160deg,#b7cfe0,#97a6a3)}

.works{display:grid;grid-template-columns:repeat(5,1fr);gap:16px}
.work .ph{height:170px}
.work .cap{background:#fff;border:1px solid var(--line);text-align:center;font-size:17px;color:var(--blue);padding:12px 0;white-space:nowrap}

/* banner */
.banner{margin-top:34px;background:linear-gradient(90deg,var(--blue-dark),var(--blue-light));height:100px;display:flex}
.banner div{flex:1;color:#fff;padding:18px 40px;border-right:1px solid rgba(255,255,255,.4)}
.banner small{display:block;font-size:13px;opacity:.85}
.banner strong{font-size:30px;font-weight:700}
.banner div:last-child{border-right:none;position:relative}
.banner .docs{position:absolute;right:40px;top:10px;width:150px;height:80px;background:linear-gradient(135deg,#f3f3f3,#cfd8e0)}

/* news */
.news{display:flex;gap:40px}
.news ul{flex:1;list-style:none}
.news li{display:flex;gap:40px;font-size:17px;padding:20px 10px;border-bottom:1px dotted var(--line)}
.news li span{color:var(--muted);width:130px;flex:none}
.news .feed{width:400px;height:420px;border:1px solid var(--line);background:linear-gradient(180deg,#f5f6f8 0 30%,#dfe6ee 30% 60%,#7a6fb8 60%,#4a3f8a)}

/* company */
.about{display:flex;gap:60px;padding:50px 0 40px;align-items:center}
.about .mark{width:300px;display:flex;align-items:center;justify-content:center;gap:14px;font-size:30px;font-weight:700;color:var(--red);flex:none}
.about .mark i{width:30px;height:30px;background:var(--red);border-radius:50%}
.about h2{font-size:26px;font-weight:700;line-height:1.6}
.about p{font-size:17px;line-height:1.8;margin-top:12px;color:var(--ink)}

/* footer */
.site-footer{margin-top:auto}
.footer{background:var(--grey);height:300px}
.footer .wrap{display:flex;gap:20px;padding-top:40px}
.fbox{width:180px;height:180px;background:#fff;display:flex;flex-direction:column;align-items:center;justify-content:center;text-align:center;font-weight:700}
.fbox.red{color:var(--red);font-size:24px}
.fbox.red small{font-size:14px;color:var(--ink);font-weight:400;margin-top:8px}
.fbox.sns{background:var(--blue-dark);color:#fff;font-size:22px}
.fbox.co{background:var(--blue);color:#fff;font-size:24px}
.fbox.blog{background:var(--green);color:#fff;font-size:26px}
.fbox.blog small{font-size:13px;font-weight:400;margin-top:8px}
.contact{color:#fff;margin-left:20px}
.contact .tel{font-size:40px;font-weight:700}
.contact p{font-size:16px;line-height:1.7}
.copy{background:var(--grey-dark);color:#eee;height:40px;display:flex;justify-content:space-between;align-items:center;padding:0 50px;font-size:14px}
</style>
</head>
<body>
<div class="page">
  <header class="header">
    <div class="wrap">
      <div class="brand"><span class="dot"></span>青嶺コンクリート工業株式会社</div>
      <nav class="util"><span>企業情報</span><span>採用情報</span><span>お問い合わせ</span><span class="login">会員ログイン</span></nav>
    </div>
  </header>

  <nav class="gnav">
    <ul><li>トップページ</li><li>製品案内</li><li>施工事例</li><li>研究開発</li><li>得意分野</li></ul>
  </nav>

  <section class="hero" role="img" aria-label="湖に浮かぶコンクリートフロートの桟橋の風景">
    <div class="hero-card">
      <div class="kicker">水域関連施設材</div>
      <h1>コンクリートフロート</h1>
      <p>コンクリートを丈夫さを活かしたフロート(浮桟橋)です。</p>
    </div>
  </section>

  <ul class="ptabs">
    <li>ロードスラブ<br>(道路橋)</li><li>ガードライン</li><li class="on">コンクリート<br>フロート</li><li>鉄道関連</li><li>道路関連</li><li>農業用</li><li>その他</li>
  </ul>

  <section class="wrap">
    <h2 class="sec-title">こんなシーンで利用されています</h2>
    <div class="scenes">
      <div class="scene"><div class="ph t1" role="img" aria-label="道路橋の写真"></div><div class="cap">道路橋に</div></div>
      <div class="scene"><div class="ph t2" role="img" aria-label="道路防護柵の写真"></div><div class="cap">道路防護柵に</div></div>
      <div class="scene"><div class="ph t3" role="img" aria-label="浮桟橋の写真"></div><div class="cap">浮桟橋に</div></div>
      <div class="scene"><div class="ph t4" role="img" aria-label="ソーラーパネルの写真"></div><div class="cap">ソーラーパネルの設置に</div></div>
      <div class="scene"><div class="ph t5" role="img" aria-label="傾斜地の写真"></div><div class="cap">傾斜地や岩場に</div></div>
      <div class="scene"><div class="ph t6" role="img" aria-label="田んぼの写真"></div><div class="cap">田んぼの区画整理に</div></div>
      <div class="scene"><div class="ph t2" role="img" aria-label="用水路の蓋の写真"></div><div class="cap">用水路の蓋に</div></div>
      <div class="scene"><div class="ph t1" role="img" aria-label="水路の橋の写真"></div><div class="cap">水路に橋を渡す</div></div>
      <div class="scene"><div class="ph t5" role="img" aria-label="歩道の写真"></div><div class="cap">歩道に設置</div></div>
    </div>

    <h2 class="sec-title">施工事例</h2>
    <div class="works">
      <div class="work"><div class="ph t1" role="img" aria-label="ロードスラブ施工事例"></div><div class="cap">ロードスラブ</div></div>
      <div class="work"><div class="ph t2" role="img" aria-label="ガードライン施工事例"></div><div class="cap">ガードライン</div></div>
      <div class="work"><div class="ph t3" role="img" aria-label="コンクリートフロート施工事例"></div><div class="cap">コンクリートフロート</div></div>
      <div class="work"><div class="ph t4" role="img" aria-label="鉄道関連製品施工事例"></div><div class="cap">鉄道関連製品</div></div>
      <div class="work"><div class="ph t6" role="img" aria-label="その他の施工事例"></div><div class="cap">その他の事例</div></div>
    </div>

    <div class="banner">
      <div><small>コンクリート製品のよく使われる用語</small><strong>コンクリート用語集</strong></div>
      <div><small>コンクリート資料を無料でお届け</small><strong>資料プレゼント</strong><span class="docs" role="img" aria-label="資料冊子のイメージ"></span></div>
    </div>

    <h2 class="sec-title">新着情報</h2>
    <div class="news">
      <ul>
        <li><span>2015年03月07日</span>SNSページオープン！</li>
        <li><span>2015年01月31日</span>ブログ更新しました。</li>
        <li><span>2015年1月28日</span>ブログ更新しました。</li>
        <li><span>2015年01月06日</span>新年明けましておめでとうございます。</li>
        <li><span>2014年12月24日</span>年末、年始のご案内</li>
        <li><span>2014年12月1日</span>ホームページリニューアル</li>
      </ul>
      <div class="feed" role="img" aria-label="SNSページのタイムラインと花の写真"></div>
    </div>
  </section>

  <section class="wrap about">
    <div class="mark"><i></i>青嶺コンクリート</div>
    <div>
      <h2>コンクリートと共に創業 50 年。<br>これからも各種コンクリート製品の研究開発を通して<br>地域に貢献できる会社を目指します。</h2>
      <p>青嶺コンクリート工業株式会社は、昭和 36 年の創業以来、<br>石川県青嶺市を基盤とする各種コンクリート二次製品の設計・<br>製品・販売・施工を行っています。</p>
    </div>
  </section>

  <footer class="site-footer">
    <div class="footer">
      <div class="wrap">
        <div class="fbox red">新商品開発<small>プレキャスト製品の<br>ご提案</small></div>
        <div class="fbox sns">SNSページ</div>
        <div class="fbox co">会社情報</div>
        <div class="fbox blog">ブログ<small>青嶺情報<br>製品情報 歴史 コラム</small></div>
        <div class="contact">
          <div class="tel">076-555-0142</div>
          <p>営業時間：8:00 - 17:00<br>定休日：日曜・祝日</p>
          <p>〒920-0000<br>石川県青嶺市中央町 1-2-3</p>
        </div>
      </div>
    </div>
    <div class="copy"><span>© 2015 Aomine Concrete Kogyo Co., Ltd.</span><span>プライバシーポリシー</span></div>
  </footer>
</div>
</body>
</html>
```